The Bright Lantern, an online college fair for non-traditional students, needs a web site

I need design and coding for a functioning web site that will serve as an online college fair that connects non-traditional students with college admissions officers and college advisors. I have chosen Wordpress and the "Meridian" theme for the site, and you can see what I already have here: https://brightlanternhub.example/
I need help setting up the site's pages and functionality, including SEO optimization and a password protected area. I will manage all content. In addition to me as the administrator, other users will be: college admissions officers, non-traditional students (like homeschoolers), and college advisors.
Target Market(s)
Homeschoolers and college/university admissions officers
Industry/Entity Type
College
Coding
Coded - Design and coding required
Number of Pages Required
5+ page
Font styles to use
Requirements
Must have
- - An inviting but professional look (see the logo as a starting point)
- - Easy to navigate
- - A way to register subscribed members (students)
- - A password-protected "members only" area
- - Virtual "booths" on the Schools page that lead to a detail page for each school
- - SEO optimized
Nice to have
- - Searchable site

```html
<!DOCTYPE html>
<html lang="en">
<head>
<meta charset="utf-8">
<title>The Bright Lantern — Online College Fair</title>
<link href="https://fonts.googleapis.com/css2?family=Montserrat:wght@400;600;700&family=Open+Sans:wght@400;600&display=swap" rel="stylesheet">
<style>
:root{
  --red:#c4161c;
  --red-dark:#a40f15;
  --ink:#2b2b2b;
  --muted:#7a7a7a;
  --line:#e2e2e2;
  --soft:#f2f2f2;
  --white:#ffffff;
}
*{box-sizing:border-box;margin:0;padding:0}
html,body{width:1200px;height:2452px;overflow:hidden}
body{font-family:"Open Sans",sans-serif;color:var(--ink);background:var(--white);position:relative}
h1,h2,h3,h4,.nav a,.btn{font-family:"Montserrat",sans-serif}
p{font-size:13px;line-height:21px;color:var(--muted)}

.topbar{height:32px;border-bottom:1px solid var(--line);display:flex;justify-content:space-between;align-items:center;padding:0 56px;font-size:12px;color:var(--muted)}
.topbar .contact span{margin-right:26px}
.topbar .account span{margin-left:22px}
.topbar .dot{display:inline-block;width:8px;height:8px;border-radius:50%;background:var(--red);margin-right:6px;vertical-align:middle}

.header{height:120px;display:flex;justify-content:space-between;align-items:center;padding:0 56px}
.brand{display:flex;align-items:center;gap:14px}
.brand-mark{width:46px;height:46px;background:var(--red)}
.brand-name{font-family:"Montserrat",sans-serif;font-weight:700;font-size:24px;color:var(--ink);letter-spacing:1px;text-transform:uppercase}
.nav{display:flex;gap:6px}
.nav a{font-size:12px;font-weight:600;color:var(--ink);text-decoration:none;text-transform:uppercase;padding:10px 14px}
.nav a.active{color:var(--red);border-bottom:2px solid var(--red)}

.hero{position:relative;height:508px;background:linear-gradient(90deg,#e9dccf 0%,#bfa893 35%,#3a3533 62%,#262322 100%)}
.hero-photo{position:absolute;left:0;top:0;width:600px;height:508px}
.hero-copy{position:absolute;left:636px;top:120px;width:470px;color:var(--white)}
.hero-copy h1{font-size:38px;line-height:48px;font-weight:600}
.hero-copy p{color:#e6e6e6;margin:22px 0 30px}
.btn{display:inline-block;font-size:14px;font-weight:600;padding:0 28px;height:46px;line-height:44px;border:1px solid var(--white);color:var(--white);margin-right:34px}
.btn.solid{background:var(--red);border-color:var(--red)}
.dots{position:absolute;left:0;right:0;bottom:18px;display:flex;justify-content:center;gap:8px}
.dots i{width:11px;height:11px;border-radius:50%;background:#bdbdbd}
.dots i.on{background:var(--white)}

.steps{height:540px;text-align:center;padding-top:72px}
.section-title{font-size:30px;font-weight:600;color:var(--ink)}
.section-title span{color:var(--red)}
.steps .intro{width:680px;margin:20px auto 0;font-size:12px;line-height:20px}
.timeline{position:relative;height:80px;margin-top:56px}
.timeline svg{position:absolute;left:0;top:0}
.step-cols{display:flex;justify-content:center;gap:78px;margin-top:16px}
.step{width:260px}
.step h3{font-size:15px;font-weight:700;color:var(--red);line-height:22px;min-height:44px}
.step p{font-size:12px;line-height:20px;margin-top:10px}

.students{height:420px;background:var(--soft);display:flex}
.students-photo{width:600px;height:420px;background:linear-gradient(135deg,#d7c7b6,#9c8572 55%,#6b5a4d)}
.students-copy{padding:44px 0 0 42px;width:520px}
.students-copy h2{font-size:30px;font-weight:600;color:var(--red)}
.students-copy .rule{width:60px;height:3px;background:var(--red);margin:12px 0 18px}
.students-copy p{font-size:12px;line-height:20px}
.ticks{list-style:none;margin:18px 0 20px}
.ticks li{font-size:12px;color:var(--muted);line-height:23px;display:flex;align-items:center;gap:8px}
.btn.small{height:30px;line-height:28px;font-size:12px;padding:0 14px;border-color:var(--red);color:var(--red);margin:0}

.testimonials{height:400px;padding:80px 100px 0}
.testimonials-head{display:flex;justify-content:space-between;align-items:center}
.testimonials-head h2{font-size:30px;font-weight:600;color:var(--red)}
.arrows{display:flex;gap:8px}
.arrows span{width:24px;height:24px;background:var(--red);display:flex;align-items:center;justify-content:center}
.quotes{display:flex;justify-content:space-between;margin-top:40px;padding:0 28px}
.quote{width:440px;border:1px solid var(--line);border-bottom:3px solid var(--red);padding:28px 30px 0;height:150px;position:relative;box-shadow:0 2px 6px rgba(0,0,0,.06)}
.quote p{font-size:13px;line-height:20px;color:#555}
.quote .who{position:absolute;left:30px;bottom:12px;font-size:11px;color:var(--muted)}

.news{height:340px;text-align:center;padding-top:34px}
.news-item{display:flex;gap:32px;text-align:left;margin:50px 0 0 112px}
.news-photo{width:220px;height:160px;background:linear-gradient(135deg,#d9c3b1,#b0372f 60%,#7d2a26)}
.news-copy{width:640px;padding-top:12px}
.news-copy .meta{font-size:11px;color:var(--muted)}
.news-copy h3{font-size:24px;font-weight:600;margin:8px 0 16px;color:var(--ink)}
.news-copy p{font-size:13px}

.footer{position:absolute;left:0;bottom:0;width:1200px;height:92px;background:var(--red-dark);color:var(--white);text-align:center;padding-top:24px}
.footer nav{display:flex;justify-content:center;gap:26px}
.footer nav a{color:var(--white);text-decoration:none;font-size:13px;font-family:"Montserrat",sans-serif}
.footer small{display:block;font-size:11px;margin-top:12px;color:#f0caca}
</style>
</head>
<body>

<div class="topbar">
  <div class="contact"><span>(415) 555-0137</span><span>hello@brightlanternhub.example</span></div>
  <div class="account"><span><i class="dot"></i>Log in</span><span><i class="dot"></i>Register</span></div>
</div>

<header class="header">
  <div class="brand"><div class="brand-mark"></div><div class="brand-name">The Bright Lantern</div></div>
  <nav class="nav">
    <a class="active">Home</a><a>Students</a><a>Schools Advisors</a><a>Member Resources</a><a>News</a><a>Contact Us</a>
  </nav>
</header>

<section class="hero">
  <div class="hero-photo" role="img" aria-label="Smiling student holding books" style="background:linear-gradient(90deg,#efe4d8,#c9ae95 60%,rgba(80,70,65,0))"></div>
  <div class="hero-copy">
    <h1>We Are Engaged To Give You A Bright Future</h1>
    <p>Lorem Ipsum is simply dummy text of the printing and typesetting industry. Lorem Ipsum has been the industry's standard dummy text ever since the 1500s Lorem Ipsum is simply dummy.</p>
    <a class="btn solid">Call Us</a><a class="btn">Learn More</a>
  </div>
  <div class="dots"><i class="on"></i><i></i><i></i><i></i></div>
</section>

<section class="steps">
  <h2 class="section-title">Get Your Success In Just <span>3</span> Steps</h2>
  <p class="intro">Lorem Ipsum is simply dummy text of the printing and typesetting industry. Lorem Ipsum has been the industry's standard dummy text ever since the 1500s Lorem Ipsum is simply dummy text of the printing and typesetting industry.</p>
  <div class="timeline">
    <svg width="1200" height="80" viewBox="0 0 1200 80">
      <line x1="0" y1="40" x2="1200" y2="40" stroke="#c4161c" stroke-width="2"/>
      <g font-family="Montserrat,sans-serif" font-weight="700" font-size="18" text-anchor="middle" fill="#fff">
        <circle cx="262" cy="40" r="24" fill="#fff" stroke="#e2e2e2" stroke-width="6"/><circle cx="262" cy="40" r="19" fill="#c4161c"/><text x="262" y="46">1</text>
        <circle cx="600" cy="40" r="24" fill="#fff" stroke="#e2e2e2" stroke-width="6"/><circle cx="600" cy="40" r="19" fill="#1e1e1e"/><text x="600" y="46">2</text>
        <circle cx="938" cy="40" r="24" fill="#fff" stroke="#e2e2e2" stroke-width="6"/><circle cx="938" cy="40" r="19" fill="#1e1e1e"/><text x="938" y="46">3</text>
      </g>
    </svg>
  </div>
  <div class="step-cols">
    <div class="step"><h3>Choose Your Course</h3><p>Lorem Ipsum is simply dummy text of the printing and typesetting industry. Lorem Ipsum has been the industry's standard dummy text ever since the 1500s.</p></div>
    <div class="step"><h3>Connect With Admissions Officers &amp; College Advisors</h3><p>Lorem Ipsum is simply dummy text of the printing and typesetting industry. Lorem Ipsum has been the industry's standard dummy text ever since the 1500s.</p></div>
    <div class="step"><h3>Make Future As Your Wish</h3><p>Lorem Ipsum is simply dummy text of the printing and typesetting industry. Lorem Ipsum has been the industry's standard dummy text ever since the 1500s.</p></div>
  </div>
</section>

<section class="students">
  <div class="students-photo" role="img" aria-label="Students writing in a classroom"></div>
  <div class="students-copy">
    <h2>Our Students</h2>
    <div class="rule"></div>
    <p>Lorem Ipsum is simply dummy text of the printing and typesetting industry. Lorem Ipsum has been the industry's standard dummy text ever since the 1500s Lorem Ipsum is simply dummy text of the printing and typesetting industry. Lorem Ipsum has been the industry's standard dummy text ever since the 1500s.</p>
    <ul class="ticks">
      <li><svg width="10" height="10"><rect width="10" height="10" fill="#c4161c"/></svg>Lorem Ipsum is simply dummy text of the printing</li>
      <li><svg width="10" height="10"><rect width="10" height="10" fill="#c4161c"/></svg>Lorem Ipsum is simply dummy text of the printing</li>
      <li><svg width="10" height="10"><rect width="10" height="10" fill="#c4161c"/></svg>Lorem Ipsum is simply dummy text of the printing</li>
      <li><svg width="10" height="10"><rect width="10" height="10" fill="#c4161c"/></svg>Lorem Ipsum is simply dummy text of the printing</li>
    </ul>
    <a class="btn small">Read More</a>
  </div>
</section>

<section class="testimonials">
  <div class="testimonials-head">
    <h2>Testimonials</h2>
    <div class="arrows">
      <span><svg width="10" height="10" viewBox="0 0 10 10"><path d="M7 1L3 5l4 4" stroke="#fff" stroke-width="2" fill="none"/></svg></span>
      <span><svg width="10" height="10" viewBox="0 0 10 10"><path d="M3 1l4 4-4 4" stroke="#fff" stroke-width="2" fill="none"/></svg></span>
    </div>
  </div>
  <div class="quotes">
    <div class="quote"><p>"Lorem Ipsum is simply dummy text of the printing and typesetting industry. Lorem Ipsum has been the industry's standard dummy text ever since the 1500s"</p><span class="who">Lorem Ipsum the Industry</span></div>
    <div class="quote"><p>"Lorem Ipsum is simply dummy text of the printing and typesetting industry. Lorem Ipsum has been the industry's standard dummy text ever since the 1500s"</p><span class="who">Lorem Ipsum the Industry</span></div>
  </div>
</section>

<section class="news">
  <h2 class="section-title">News</h2>
  <div class="news-item">
    <div class="news-photo" role="img" aria-label="Student studying with a laptop"></div>
    <div class="news-copy">
      <div class="meta">Welcome to The Bright Lantern &nbsp;·&nbsp; Lorem Ipsum</div>
      <h3>Here's a sneak peek at what we're working on….!</h3>
      <p>The Bright Lantern is a new web site designed to provide a meeting place for college and university admission officers and non-traditional applicants.</p>
    </div>
  </div>
</section>

<footer class="footer">
  <nav><a>Home</a><a>Students</a><a>Schools Advisors</a><a>Member Resources</a><a>News</a><a>Contact Us</a></nav>
  <small>© 2017 The Bright Lantern. All rights reserved. Terms of Use</small>
</footer>

</body>
</html>
```